Pomelo - Website for fruit & juice

- The location of the outlet is Fort Kochi in India.
- Fort Kochi is a tourist destination. And it attracts majorly French and Portuguese tourist due to the history of the place.
- The location had plenty of food joints & mostly provide local foods only without giving much options to tourist.
- Road side fruit shops don't look hygienic
- At Pomelo we are going to sell fresh fruits as well as fruit juices.
- Customers can pick their fruits and Pomelo staffs will squeeze/blend or slice it for them.
- There will be no e-commerce on the site (no buying of products through site)

Target Market(s)

Tourist & health conscious individuals who want to have fresh fruit or juice.

Coding

Coded - Design and coding required

Number of Pages Required

4 page

Font styles to use
Script

Colors

Designer to choose colors to be used in the design.

Requirements
Must have
• Back End. Editable website.
• Since it for fruits & juices, we will be selling fruits as per season or availability.
• Editable or back end will allow us to add or delete menus as per availability.
• The project much have 4 pages. Namely:
• - Home
• - Concept
• - Menu
• - Location & Contact
Nice to have
• Fresh feel of the website
Should not have
• E-commerce

```html
<!DOCTYPE html>
<html lang="en">
<head>
<meta charset="utf-8">
<title>Pomelo – Fresh Fruit &amp; Juice, Fort Kochi</title>
<link rel="stylesheet" href="https://fonts.googleapis.com/css2?family=Lobster&family=Roboto:wght@400;500;700&display=swap">
<style>
:root{
  --green:#1e7a1e;
  --green-dark:#185f18;
  --orange:#ff5a0a;
  --orange-light:#ff8a1e;
  --ink:#222;
  --text:#444;
  --muted:#666;
  --grey-band:#f1f1f1;
  --white:#fff;
}
*{box-sizing:border-box;margin:0;padding:0}
html,body{width:1200px;height:3953px;overflow:hidden}
body{position:relative;background:var(--white);font-family:'Roboto',Arial,sans-serif;color:var(--text)}
.abs{position:absolute}
.script{font-family:'Lobster',cursive;color:var(--ink);font-weight:400}
.btn{position:absolute;display:flex;align-items:center;justify-content:center;gap:6px;height:49px;border-radius:25px;color:#fff;font-weight:700;font-size:16px;text-decoration:none}
.btn--orange{background:var(--orange)}
.btn--green{background:var(--green)}
.btn .arrow{width:14px;height:14px}

/* header */
.topline{top:0;left:0;width:1200px;height:3px;background:var(--green)}
.topline--orange{left:1086px;width:114px;background:var(--orange)}
.tab{top:0;height:40px;display:flex;align-items:center;justify-content:center;gap:5px;color:#fff;font-weight:700;font-size:17px}
.tab--visit{left:733px;width:164px;background:var(--green);border-radius:0 0 0 22px}
.tab--contact{left:897px;width:189px;background:var(--orange);border-radius:0 0 22px 0}
.brand{display:flex;align-items:center;gap:10px;font-weight:700;font-size:52px;color:var(--green);letter-spacing:-1px}
.brand__dot{width:22px;height:22px;border-radius:50%;background:var(--orange)}
.nav{top:97px;left:536px;display:flex;gap:0;font-weight:500;font-size:17px;color:var(--ink)}
.nav a{position:absolute;white-space:nowrap;color:var(--ink);text-decoration:none}

/* hero */
.hero-photo{top:169px;left:0;width:1200px;height:790px;
  background:radial-gradient(ellipse at 30% 30%,#d8363a 0,#b01d26 22%,transparent 40%),
             radial-gradient(ellipse at 45% 75%,#c82a2f 0,#9c1a22 20%,transparent 36%),
             linear-gradient(110deg,#2f4d1c 0%,#5e7d2a 40%,#8aa23a 70%,#a7b94e 100%)}
.hero-title{top:318px;left:640px;font-size:80px;color:#fff;text-shadow:0 2px 6px rgba(0,0,0,.35)}
.hero-sub{top:423px;left:640px;width:460px;font-size:20px;font-weight:500;line-height:29px;color:#fff;text-shadow:0 1px 3px rgba(0,0,0,.4)}

/* concept */
.section-title{font-size:54px;text-align:center;width:1200px;left:0}
.concept-text{top:1052px;left:150px;width:900px;text-align:center;font-size:16px;line-height:31.5px;color:var(--text)}
.concept-text strong{color:var(--green)}

/* menu */
.menu-title{top:1548px;left:120px;font-size:52px}
.menu-lead{top:1618px;left:124px;font-size:15px;color:var(--ink)}
.drink{width:150px;height:215px;top:1673px;border-radius:10px 10px 30px 30px}
.drink-name{top:1918px;width:220px;text-align:center;font-weight:500;font-size:21px;letter-spacing:1.5px;color:var(--ink)}
.circle-arrow{width:42px;height:42px;border:2px solid var(--orange);border-radius:50%;top:1994px}

/* about */
.about-bg{top:2180px;left:0;width:1200px;height:660px;background:linear-gradient(180deg,#fff 0%,#fbf7f2 40%,#f6efe6 100%)}
.about-photo{left:100px;top:2243px;width:430px;height:430px;border-radius:50%;
  background:radial-gradient(circle at 60% 35%,#e8e2d6 0,#cfc6b5 20%,transparent 35%),
             linear-gradient(160deg,#7e8a3a 0%,#e0a43a 35%,#e56a2a 60%,#7c5a3a 100%)}
.about-title{top:2232px;left:596px;font-size:52px}
.about-text{left:603px;width:485px;font-size:16px;line-height:29.3px;color:var(--text);text-align:justify}
.divider{top:2804px;left:110px;width:978px;height:1px;background:#ddd}

/* reviews */
.review-avatar{width:62px;height:62px;border-radius:50%;top:3004px;background:linear-gradient(160deg,#cfd3d6,#8c8f93)}
.review-badge{width:18px;height:18px;border-radius:50%;top:3057px}
.stars{top:3007px;display:flex;gap:3px}
.review-text{top:3030px;width:222px;font-size:15px;line-height:29px;font-style:italic;color:var(--muted);text-align:justify}
.review-name{top:3164px;font-weight:500;font-size:15px;color:var(--ink)}
.review-role{top:3187px;font-size:15px;color:var(--muted)}
.chev{top:3066px;width:24px;height:24px}

/* footer */
.footer{top:3300px;left:0;width:1200px;height:653px;background:linear-gradient(180deg,#227a22,#1a5f1a)}
.footer-brand{top:3424px;left:822px;color:#fff;font-size:80px}
.foot-head{top:3588px;font-weight:500;font-size:17px;color:#fff;white-space:nowrap}
.foot-list{top:3627px;list-style:none;color:#fff;font-size:14px;line-height:29px}
.foot-list li::before{content:"»";margin-right:12px}
.contact-line{display:flex;gap:14px;color:#fff;font-size:14px;line-height:20px;position:absolute;left:526px}
.newsletter-text{top:3630px;left:822px;width:270px;color:#fff;font-size:14px;line-height:20px}
.email-field{top:3678px;left:823px;width:264px;height:34px;border:1px solid rgba(255,255,255,.8);color:#fff;font-size:11px;padding:8px 12px}
.subscribe{top:3729px;left:823px;width:107px;height:34px;border-radius:17px;background:var(--orange);color:#fff;font-size:12px;font-weight:500;display:flex;align-items:center;justify-content:center}
.foot-rule{top:3826px;height:1px;background:rgba(255,255,255,.7)}
.social{top:3809px;width:36px;height:36px;border:2px solid #fff;border-radius:50%}
.copyright{top:3870px;left:0;width:1200px;text-align:center;color:#fff;font-size:15px}
</style>
</head>
<body>

<!-- Header -->
<div class="abs topline"></div>
<div class="abs topline topline--orange"></div>
<div class="abs tab tab--visit">
  <svg width="12" height="16" viewBox="0 0 12 16"><path d="M6 0a6 6 0 0 0-6 6c0 4.5 6 10 6 10s6-5.5 6-10a6 6 0 0 0-6-6zm0 8.5A2.5 2.5 0 1 1 6 3.5a2.5 2.5 0 0 1 0 5z" fill="#fff"/></svg>VISIT US</div>
<div class="abs tab tab--contact">
  <svg width="15" height="15" viewBox="0 0 16 16"><path d="M3.6 1l2.6 3-1.5 1.8c.9 2 2.5 3.6 4.5 4.5L11 8.8l3 2.6-1.4 2.9C7 14.3 1.7 9 1.7 3.4z" fill="#fff"/></svg>CONTACT US</div>
<div class="abs brand" style="top:52px;left:110px">Pomelo<span class="brand__dot"></span></div>
<nav class="abs nav">
  <a style="left:0">HOME</a>
  <a style="left:86px">CONCEPT</a>
  <a style="left:204px">MENU</a>
  <a style="left:290px">ABOUT US</a>
  <a style="left:412px">LOCATION</a>
  <svg style="position:absolute;left:536px;top:2px" width="16" height="16" viewBox="0 0 16 16"><circle cx="6.5" cy="6.5" r="5" fill="none" stroke="#222" stroke-width="2.2"/><path d="M10.5 10.5L15 15" stroke="#222" stroke-width="2.4"/></svg>
</nav>

<!-- Hero -->
<div class="abs hero-photo" role="img" aria-label="Close-up photo of ripe red apples with water droplets hanging among green leaves"></div>
<div class="abs script hero-title">Feel Fresh</div>
<p class="abs hero-sub">We make juice from the fresh fruits that you pick up yourself from the fruit basket.</p>
<a class="btn btn--orange" style="top:509px;left:640px;width:196px">READ MORE
  <svg class="arrow" viewBox="0 0 16 16"><circle cx="8" cy="8" r="8" fill="#fff"/><path d="M4 8h7M8 4.5L11.5 8 8 11.5" stroke="var(--orange)" stroke-width="2" fill="none"/></svg></a>
<svg class="abs" style="top:650px;left:0" width="1200" height="310" viewBox="0 0 1200 310">
  <path d="M0,70 C150,195 350,215 560,175 C760,135 950,75 1200,110 L1200,310 L0,310Z" fill="#fff"/>
  <path d="M330,200 C580,175 790,55 980,52 C1100,50 1170,85 1200,105 L1200,294 C1130,190 1050,150 950,148 C750,146 560,205 330,200Z" fill="var(--orange)"/>
  <path d="M420,198 C640,185 820,120 960,120 C1060,120 1140,160 1200,210 L1200,230 C1130,175 1050,145 950,145 C760,145 600,200 420,198Z" fill="var(--orange-light)"/>
</svg>

<!-- Concept -->
<h2 class="abs script section-title" style="top:955px">Origin Of The Concept</h2>
<p class="abs concept-text">Visit any fruit vendor and ask them what they do with the left over and if you are lucky enough you<br>may get the truth. <strong>“They sell their leftover to the juice bar”</strong> When you order a glass of juice from any place you<br>may not have any idea about the condition of the fruit before it was squeezed &amp; served<br>to you. Here is where we at Pomelo wanted to bring in transparency.</p>
<a class="btn btn--orange" style="top:1221px;left:390px;width:195px">READ MORE
  <svg class="arrow" viewBox="0 0 16 16"><circle cx="8" cy="8" r="8" fill="#fff"/><path d="M4 8h7M8 4.5L11.5 8 8 11.5" stroke="var(--orange)" stroke-width="2" fill="none"/></svg></a>
<a class="btn btn--green" style="top:1221px;left:615px;width:195px">CONTACT US
  <svg class="arrow" viewBox="0 0 16 16"><circle cx="8" cy="8" r="8" fill="#fff"/><path d="M4 8h7M8 4.5L11.5 8 8 11.5" stroke="var(--green)" stroke-width="2" fill="none"/></svg></a>

<!-- Menu band -->
<svg class="abs" style="top:1400px;left:0" width="1200" height="760" viewBox="0 0 1200 760">
  <path d="M0,142 C150,45 300,12 460,20 L1200,135 L1200,610 C1100,700 900,745 700,738 L0,600Z" fill="var(--grey-band)"/>
  <path d="M0,140 C150,40 300,2 470,12 C300,25 150,72 0,156Z" fill="var(--green)"/>
  <path d="M450,688 C700,742 1000,722 1200,600 L1200,625 C1000,760 700,765 450,688Z" fill="var(--green)"/>
</svg>
<h2 class="abs script menu-title">Our Menu</h2>
<p class="abs menu-lead">Lorem ipsum dolor sit amet consectetur adipiscing elit sed do eiusmod tempor incididunt.</p>
<div class="abs drink" style="left:94px;background:linear-gradient(180deg,#b049a8,#6b1d6e 70%,#2a1a2a)" role="img" aria-label="Glass of blackberry juice with fresh blackberries"></div>
<div class="abs drink" style="left:307px;background:linear-gradient(180deg,#ffb6c4,#f26e8c 70%,#d0202e)" role="img" aria-label="Glass of strawberry smoothie with strawberries"></div>
<div class="abs drink" style="left:530px;background:linear-gradient(180deg,#ff5a5a,#e0141e 70%,#3f8a2a)" role="img" aria-label="Glass of watermelon juice with watermelon slices"></div>
<div class="abs drink" style="left:751px;background:linear-gradient(180deg,#a03050,#5a0f25 70%,#1d1a2a)" role="img" aria-label="Glass of black currant juice with berries"></div>
<div class="abs drink" style="left:953px;background:linear-gradient(180deg,#f6c8a0,#f0a070 60%,#d83a2a)" role="img" aria-label="Glass of mint juice with a cut peach"></div>
<div class="abs drink-name" style="left:59px">BLACKBERRY</div>
<div class="abs drink-name" style="left:272px">STRAWBERRY</div>
<div class="abs drink-name" style="left:495px">WATERMELON</div>
<div class="abs drink-name" style="left:716px">BLACK CURRANT</div>
<div class="abs drink-name" style="left:918px">MINT JUICE</div>
<div class="abs circle-arrow" style="left:929px"><svg width="38" height="38" viewBox="0 0 38 38"><path d="M22 11l-8 8 8 8" stroke="var(--orange)" stroke-width="2.2" fill="none"/></svg></div>
<div class="abs circle-arrow" style="left:989px"><svg width="38" height="38" viewBox="0 0 38 38"><path d="M16 11l8 8-8 8" stroke="var(--orange)" stroke-width="2.2" fill="none"/></svg></div>

<!-- About -->
<div class="abs about-bg" role="img" aria-label="Soft background of fresh fruits splashing in water"></div>
<svg class="abs" style="top:2225px;left:80px" width="470" height="470" viewBox="0 0 470 470">
  <path d="M235,8 A227,227 0 1 0 462,235 A218,218 0 0 1 235,8Z" fill="var(--orange)" transform="rotate(-8 235 235)"/>
</svg>
<div class="abs about-photo" role="img" aria-label="Woman in an apron picking fresh fruit in a market aisle"></div>
<h2 class="abs script about-title">About Pomelo</h2>
<p class="abs about-text" style="top:2325px">As a health conscious customer, one has every right to know the fruit before she/he sips the first sip of juice made out of it.</p>
<p class="abs about-text" style="top:2403px">We at Pomelo insist our clientele to pick the fresh fruits themselves from our fruit baskets so they know what they are consuming. And we can blend or squeezed those fruits for them as per their wish i.e only fruit or fruit with some add-ons. And hence we don't sell juice by bottle size rather it is all the juice that we will get from the fruits that you pick up from our fruit basket.</p>
<a class="btn btn--orange" style="top:2610px;left:605px;width:195px">READ MORE
  <svg class="arrow" viewBox="0 0 16 16"><circle cx="8" cy="8" r="8" fill="#fff"/><path d="M4 8h7M8 4.5L11.5 8 8 11.5" stroke="var(--orange)" stroke-width="2" fill="none"/></svg></a>
<div class="abs divider"></div>

<!-- Reviews -->
<h2 class="abs script section-title" style="top:2892px">Customer Reviews</h2>
<svg class="abs chev" style="left:38px" viewBox="0 0 24 24"><path d="M15 4l-8 8 8 8" stroke="#666" stroke-width="2" fill="none"/></svg>
<svg class="abs chev" style="left:1137px" viewBox="0 0 24 24"><path d="M9 4l8 8-8 8" stroke="#666" stroke-width="2" fill="none"/></svg>

<div class="abs review-avatar" style="left:112px;background:linear-gradient(160deg,#d9b9a5,#7a4a3a)" role="img" aria-label="Customer portrait"></div>
<div class="abs review-badge" style="left:134px;background:var(--green)"></div>
<div class="abs stars" style="left:189px"><svg width="90" height="15" viewBox="0 0 90 15"><g fill="var(--orange-light)"><path id="st" d="M7.5 0l2.2 4.6 5 .6-3.7 3.4 1 5-4.5-2.5L3 13.6l1-5L.3 5.2l5-.6z"/><use href="#st" x="18"/><use href="#st" x="36"/><use href="#st" x="54"/><use href="#st" x="72"/></g></svg></div>
<p class="abs review-text" style="left:189px">“ At vero eos et accusamus et iustodio dignissimos ducimus qui blanditiipraesnt ium voluptatum deleniti atque corrupti ”</p>
<div class="abs review-name" style="left:189px">MIRA DSOUZA,</div>
<div class="abs review-role" style="left:189px">Creative Manager, USA</div>

<div class="abs review-avatar" style="left:454px" role="img" aria-label="Customer portrait"></div>
<div class="abs review-badge" style="left:476px;background:var(--orange)"></div>
<div class="abs stars" style="left:531px"><svg width="90" height="15" viewBox="0 0 90 15"><g fill="var(--orange-light)"><use href="#st"/><use href="#st" x="18"/><use href="#st" x="36"/><use href="#st" x="54"/><use href="#st" x="72"/></g></svg></div>
<p class="abs review-text" style="left:531px">“ At vero eos et accusamus et iustodio dignissimos ducimus qui blanditiipraesnt ium voluptatum deleniti atque corrupti ”</p>
<div class="abs review-name" style="left:531px">ARUN THOMAS,</div>
<div class="abs review-role" style="left:531px">Creative Manager, USA</div>

<div class="abs review-avatar" style="left:793px" role="img" aria-label="Customer portrait"></div>
<div class="abs review-badge" style="left:815px;background:var(--green)"></div>
<div class="abs stars" style="left:869px"><svg width="90" height="15" viewBox="0 0 90 15"><g fill="var(--orange-light)"><use href="#st"/><use href="#st" x="18"/><use href="#st" x="36"/><use href="#st" x="54"/><use href="#st" x="72"/></g></svg></div>
<p class="abs review-text" style="left:869px">“ At vero eos et accusamus et iustodio dignissimos ducimus qui blanditiipraesnt ium voluptatum deleniti atque corrupti ”</p>
<div class="abs review-name" style="left:869px">PAULO MENDES,</div>
<div class="abs review-role" style="left:869px">Creative Manager, USA</div>

<!-- Footer -->
<div class="abs footer"></div>
<svg class="abs" style="top:3225px;left:0" width="1200" height="200" viewBox="0 0 1200 200">
  <path d="M0,0 L1200,0 L1200,40 C950,45 700,140 450,150 C250,158 90,110 0,60Z" fill="#fff"/>
  <path d="M0,20 C100,120 300,160 500,140 C800,110 1000,40 1200,38 L1200,75 C1000,75 800,135 500,170 C260,198 80,150 0,95Z" fill="var(--orange)"/>
  <path d="M0,60 C120,140 320,165 520,150 C780,128 1000,70 1200,62 L1200,72 C1000,78 780,138 520,162 C300,180 110,150 0,80Z" fill="var(--orange-light)"/>
</svg>
<div class="abs footer-brand" style="font-family:'Roboto',sans-serif;font-weight:700;font-size:64px;top:3440px">Pomelo</div>

<div class="abs foot-head" style="left:110px">QUICK LINKS</div>
<ul class="abs foot-list" style="left:110px"><li>Home</li><li>Concept</li><li>Menu</li><li>About Us</li><li>Location</li></ul>
<div class="abs foot-head" style="left:315px">OTHER LINKS</div>
<ul class="abs foot-list" style="left:315px"><li>Reviews</li><li>Taste</li><li>Terms &amp; Conditiond</li><li>FAQs</li><li>Contact Us</li></ul>
<div class="abs foot-head" style="left:526px">CONTACT US</div>
<div class="contact-line" style="top:3630px"><svg width="12" height="16" viewBox="0 0 12 16"><path d="M6 0a6 6 0 0 0-6 6c0 4.5 6 10 6 10s6-5.5 6-10a6 6 0 0 0-6-6zm0 8.5A2.5 2.5 0 1 1 6 3.5a2.5 2.5 0 0 1 0 5z" fill="#fff"/></svg><span>18 Bastion Lane,<br>Fort Kochi 682001.</span></div>
<div class="contact-line" style="top:3692px"><svg width="13" height="13" viewBox="0 0 16 16"><path d="M3.6 1l2.6 3-1.5 1.8c.9 2 2.5 3.6 4.5 4.5L11 8.8l3 2.6-1.4 2.9C7 14.3 1.7 9 1.7 3.4z" fill="#fff"/></svg><span>(+91) 484 555 0142</span></div>
<div class="contact-line" style="top:3733px"><svg width="14" height="12" viewBox="0 0 14 12" style="margin-top:4px"><rect width="14" height="10" fill="#fff"/><path d="M0 0l7 5 7-5" stroke="#1e6f1e" stroke-width="1.4" fill="none"/></svg><span>hello@pomelofresh.example</span></div>
<div class="abs foot-head" style="left:822px">NEWSLETTER SUBSCRIPTION</div>
<p class="abs newsletter-text">Register your Email Address to get more Information about us</p>
<div class="abs email-field">Email Address</div>
<div class="abs subscribe">SUBSCRIBE</div>

<div class="abs foot-rule" style="left:110px;width:400px"></div>
<div class="abs foot-rule" style="left:690px;width:398px"></div>
<div class="abs social" style="left:513px" aria-label="Social link"></div>
<div class="abs social" style="left:559px" aria-label="Social link"></div>
<div class="abs social" style="left:605px" aria-label="Social link"></div>
<div class="abs social" style="left:651px" aria-label="Social link"></div>
<p class="abs copyright">Copyrights © 2019 Pomelo.&nbsp; All Rights Reserved &nbsp;&nbsp; | &nbsp;&nbsp; Privacy Policy.</p>

</body>
</html>
```